Web design for an intellectual property law practice

I need to design a simple landing page that may in the future expand to a full site. It should be very high tech focused.

Target Market(s)

Anyone seeking legal services

Industry/Entity Type

Legal

Number of Pages Required

2 page

Font styles to use
Other font styles liked:
• The same font as my logo

Colors
ec1f27

Requirements
Must have
• My logo (see attached).
Nice to have
• Open to ideas.

```html
<!DOCTYPE html>
<html lang="en">
<head>
<meta charset="utf-8">
<title>ipnorthlegal – Intellectual Property Law</title>
<link href="https://fonts.googleapis.com/css2?family=Lato:wght@300;400;700;900&display=swap" rel="stylesheet">
<style>
:root{
  --red:#ec1f27;
  --ink:#1b1b1b;
  --text:#555;
  --muted:#8a8a8a;
  --light:#f2f2f2;
  --line:#dcdcdc;
  --navy:#0f2342;
  --footer:#1d1d1f;
  --white:#fff;
}
*{box-sizing:border-box;margin:0;padding:0}
html,body{width:1200px;height:4467px;overflow:hidden}
body{font-family:'Lato',sans-serif;color:var(--text);background:var(--white);position:relative}
section,header,footer{position:absolute;left:0;width:1200px}
.abs{position:absolute}
.btn{position:absolute;display:flex;align-items:center;justify-content:center;gap:8px;border-radius:30px;font-weight:900;font-size:15px;text-transform:uppercase;letter-spacing:.3px}
.btn-red{background:var(--red);color:var(--white)}
.section-title{position:absolute;left:0;width:100%;text-align:center;font-size:46px;color:var(--ink);font-weight:400}
.section-title b{font-weight:900}
.section-sub{position:absolute;left:0;width:100%;text-align:center;font-size:14px;color:var(--muted)}

/* header */
.site-header{top:0;height:180px;background:var(--white)}
.brand{left:110px;top:30px;width:220px;text-align:center}
.brand-mark{width:74px;height:74px;border-radius:50%;border:3px solid var(--ink);margin:0 auto 10px}
.brand-name{font-size:26px;font-weight:700;color:var(--ink);letter-spacing:-.3px}
.header-phone{right:112px;top:46px;display:flex;align-items:center;gap:12px;font-size:27px;font-weight:700;color:var(--ink)}
.main-nav{right:112px;top:120px;display:flex;gap:44px;font-size:16px;font-weight:700;color:var(--ink)}

/* hero */
.hero{top:180px;height:615px;background:linear-gradient(160deg,#1f3f7a 0%,#2a5aa8 35%,#0f1b35 70%,#3a1a3a 100%)}
.hero-title{left:625px;top:200px;font-size:58px;font-weight:900;color:var(--white);line-height:62px}
.hero-lead{left:625px;top:355px;font-size:15px;font-weight:700;color:var(--white)}
.hero .btn{left:627px;top:403px;width:176px;height:48px}

/* services */
.services{top:795px;height:780px}
.service-card{position:absolute;top:240px;width:305px;height:400px;background:var(--white);box-shadow:0 2px 10px rgba(0,0,0,.18)}
.service-media{position:absolute;left:8px;top:8px;right:8px;height:196px}
.service-card h3{position:absolute;top:218px;left:0;width:100%;text-align:center;font-size:23px;font-weight:700;color:var(--ink);line-height:30px;padding:0 20px}
.service-card p{position:absolute;left:30px;right:30px;text-align:center;font-size:14px;line-height:24px;color:var(--muted)}
.services .btn{left:527px;top:612px;width:146px;height:40px;font-size:14px}

/* about */
.about{top:1575px;height:765px;background:linear-gradient(180deg,#f3f3f3,#ececec)}
.about-photo{left:110px;top:220px;width:465px;height:210px}
.about h4{position:absolute;left:112px;top:462px;font-size:20px;color:var(--ink);font-weight:700}
.about-copy{position:absolute;left:112px;width:465px;font-size:14px;line-height:23px;color:var(--muted)}
.faq-label{left:648px;top:220px;font-size:21px;font-weight:700;color:var(--ink)}
.faq-item{position:absolute;left:650px;width:436px;height:42px;background:var(--white);border:1px solid var(--line);font-size:14px;color:var(--muted);display:flex;align-items:center;padding-left:18px}
.faq-item .toggle{position:absolute;right:0;top:-1px;width:42px;height:42px;background:var(--red);display:flex;align-items:center;justify-content:center}
.faq-item.open{background:var(--red);color:var(--white);border-color:var(--red)}
.faq-item.open .toggle{background:var(--white);border:2px solid var(--red)}
.faq-answer{position:absolute;left:650px;top:372px;width:436px;font-size:14px;line-height:24px;color:var(--text)}

/* testimonials */
.testimonials{top:2340px;height:580px;background:linear-gradient(180deg,#fff,#f7f7f7)}
.testimonial{position:absolute;top:200px;width:410px;height:218px;background:var(--white);box-shadow:0 2px 10px rgba(0,0,0,.14);padding:28px 30px}
.testimonial.faded{opacity:.35;box-shadow:none;background:transparent}
.avatar{position:absolute;left:30px;top:28px;width:66px;height:66px;border-radius:50%;background:linear-gradient(135deg,#b7a08a,#6c5a4c)}
.t-name{position:absolute;left:112px;top:36px;font-size:26px;color:var(--ink)}
.t-role{position:absolute;left:112px;top:72px;font-size:13px;color:var(--muted)}
.t-quote{position:absolute;left:30px;right:30px;top:118px;font-size:14px;line-height:24px;color:var(--text)}
.slider-arrow{position:absolute;top:440px;width:48px;height:48px;border-radius:50%;display:flex;align-items:center;justify-content:center}
.slider-arrow.prev{left:976px;background:var(--white);box-shadow:0 1px 6px rgba(0,0,0,.25)}
.slider-arrow.next{left:1040px;background:var(--red)}

/* lawyer band */
.lawyer-band{top:2920px;height:170px;background:var(--red)}
.lawyer-photo{position:absolute;left:160px;top:2800px;width:195px;height:290px;background:linear-gradient(180deg,#d9d9d9,#7c7f86 60%,#2c2f36);z-index:2}
.lawyer-name{left:400px;top:40px;font-size:26px;font-weight:900;color:var(--white);text-transform:uppercase}
.lawyer-name em{font-size:14px;font-weight:400;text-transform:none;margin-left:6px}
.lawyer-desc{left:400px;top:92px;width:500px;font-size:14px;font-weight:700;line-height:24px;color:var(--white)}
.lawyer-band .btn{left:922px;top:65px;width:164px;height:42px;background:var(--white);color:var(--red);font-size:14px}

/* partners */
.partners{top:3090px;height:360px}
.partner{position:absolute;top:175px;width:170px;height:85px;background:var(--white);border:1px solid var(--line);display:flex;align-items:center;justify-content:center}
.partner span{display:block;width:96px;height:32px;background:#3a3a3a;border-radius:3px}
.partner-arrow{position:absolute;top:205px}

/* consultation */
.consult{top:3450px;height:555px;background:linear-gradient(180deg,#f4f4f4,#ececec)}
.call-btn{position:absolute;left:480px;top:180px;width:240px;height:44px;background:var(--navy);color:var(--white);font-size:20px;font-weight:700;display:flex;align-items:center;justify-content:center;border-radius:3px}
.field{position:absolute;height:40px;background:#dedede;border:1px solid #c8c8c8;font-size:12px;color:var(--muted);padding:12px 14px}
.consult .btn{left:520px;top:415px;width:162px;height:42px}

/* footer */
.site-footer{top:4005px;height:462px;background:var(--footer);color:#d8d8d8}
.footer-brand{left:110px;top:105px;width:250px;text-align:center}
.footer-brand .brand-mark{border-color:var(--white)}
.footer-brand .brand-name{color:var(--white)}
.footer-col{position:absolute;top:100px}
.footer-col h5{font-size:17px;font-weight:900;color:var(--white);margin-bottom:30px;text-transform:uppercase}
.footer-col li{list-style:none;font-size:14px;margin-bottom:18px;display:flex;align-items:center;gap:10px}
.contact-list li{align-items:flex-start;line-height:21px;margin-bottom:22px}
.footer-rule{left:200px;top:350px;width:800px;height:1px;background:#5a5a5a}
.socials{left:490px;top:330px;display:flex;gap:14px;padding:0 16px;background:var(--footer)}
.socials span{width:40px;height:40px;border:2px solid #d8d8d8;border-radius:50%;display:block}
.copyright{left:0;top:410px;width:1200px;text-align:center;font-size:14px}
</style>
</head>
<body>

<header class="site-header">
  <div class="abs brand"><div class="brand-mark"></div><div class="brand-name">ipnorthlegal</div></div>
  <div class="abs header-phone">
    <svg width="38" height="38" viewBox="0 0 24 24"><path fill="#ec1f27" d="M6.6 10.8a15.1 15.1 0 006.6 6.6l2.2-2.2a1 1 0 011-.25 11.4 11.4 0 003.6.57 1 1 0 011 1V20a1 1 0 01-1 1A17 17 0 013 4a1 1 0 011-1h3.5a1 1 0 011 1 11.4 11.4 0 00.57 3.6 1 1 0 01-.25 1z"/></svg>
    (416) 555-0142
  </div>
  <nav class="abs main-nav"><span>HOME</span><span>ABOUT US</span><span>SERVICES</span><span>TEAM</span><span>BLOG</span><span>CONTACT US</span></nav>
</header>

<section class="hero" role="img" aria-label="Night view of the Toronto city hall square with lit sign and towers">
  <h1 class="abs hero-title">Canadian Patent<br>Lawyer</h1>
  <p class="abs hero-lead">DANIEL R. HARTLEY is a partner with LINDGREN HALE in its Toronto Office.</p>
  <span class="btn btn-red">Read more
    <svg width="16" height="16" viewBox="0 0 16 16"><circle cx="8" cy="8" r="7" fill="#fff"/><path d="M6.5 4.5l3.5 3.5-3.5 3.5" stroke="#ec1f27" stroke-width="2" fill="none"/></svg></span>
</section>

<section class="services">
  <h2 class="section-title" style="top:100px"><b>Our</b> Services</h2>
  <p class="section-sub" style="top:180px">Daniel has been sought after by national and international media as a commentator on IP matters.</p>

  <article class="service-card" style="left:110px">
    <div class="service-media" role="img" aria-label="Engineer working on a design at a computer" style="background:linear-gradient(135deg,#c9b79c,#6d5a48)"></div>
    <h3>Patents &amp; Industrial<br>Designs</h3>
    <p style="top:290px">As a registered patent agent with the national Intellectual Property Office, Daniel's practice focuses</p>
  </article>
  <article class="service-card" style="left:447px">
    <div class="service-media" role="img" aria-label="Desk with documents and a laptop" style="background:linear-gradient(135deg,#e7e4de,#9a958c)"></div>
    <h3>Trademark Protection</h3>
    <p style="top:262px">As a registered trademark agent, Daniel advises local, national and international clients on how to efficiently</p>
  </article>
  <article class="service-card" style="left:783px">
    <div class="service-media" role="img" aria-label="Business meeting with contracts on a table" style="background:linear-gradient(135deg,#8e7a66,#3d3a3c)"></div>
    <h3>Commercial Intellectual<br>Property</h3>
    <p style="top:290px">Daniel is frequently called upon to advise clients on commercializing intellectual property rights, including</p>
  </article>
  <span class="btn btn-red">Read more
    <svg width="14" height="14" viewBox="0 0 16 16"><circle cx="8" cy="8" r="7" fill="#fff"/><path d="M6.5 4.5l3.5 3.5-3.5 3.5" stroke="#ec1f27" stroke-width="2" fill="none"/></svg></span>
</section>

<section class="about">
  <h2 class="section-title" style="top:92px"><b>About</b> ipnorthlegal</h2>
  <p class="section-sub" style="top:160px">Daniel has been sought after by national and international media as a commentator on IP matters.</p>
  <div class="abs about-photo" role="img" aria-label="Three lawyers reviewing documents at a table" style="background:linear-gradient(135deg,#e9edf2,#8a8f98 55%,#2d2f35)"></div>
  <h4>CANADIAN PATENT LAWYER</h4>
  <p class="about-copy" style="top:505px">Daniel has been sought after by national and international media as a commentator on IP matters.</p>
  <p class="about-copy" style="top:565px">Daniel speaks and writes extensively on all aspects of intellectual property rights, particularly the commercialization of IP rights for start-ups as well as commercial matters for companies with respect to IP rights in national, cross-border and multinational commercial transactions.</p>

  <div class="abs faq-label">FAQ'S</div>
  <div class="faq-item" style="top:270px">Why IP Matters to Your StartUp<span class="toggle"><svg width="14" height="14" viewBox="0 0 14 14"><path d="M5 2l5 5-5 5" stroke="#fff" stroke-width="2" fill="none"/></svg></span></div>
  <div class="faq-item open" style="top:320px">Why IP Matters to Your StartUp<span class="toggle"><svg width="14" height="14" viewBox="0 0 14 14"><path d="M2 5l5 5 5-5" stroke="#ec1f27" stroke-width="2" fill="none"/></svg></span></div>
  <p class="faq-answer">Lorem ipsum dolor sit amet, consectetur adipiscing elit, sed do eiusmod tempor incididunt ut labore et dolore magna aliqua. Ut enim ad minim veniam...</p>
  <div class="faq-item" style="top:475px">Why IP Matters to Your StartUp<span class="toggle"><svg width="14" height="14" viewBox="0 0 14 14"><path d="M5 2l5 5-5 5" stroke="#fff" stroke-width="2" fill="none"/></svg></span></div>
  <div class="faq-item" style="top:525px">Why IP Matters to Your StartUp<span class="toggle"><svg width="14" height="14" viewBox="0 0 14 14"><path d="M5 2l5 5-5 5" stroke="#fff" stroke-width="2" fill="none"/></svg></span></div>
  <div class="faq-item" style="top:575px">Why IP Matters to Your StartUp<span class="toggle"><svg width="14" height="14" viewBox="0 0 14 14"><path d="M5 2l5 5-5 5" stroke="#fff" stroke-width="2" fill="none"/></svg></span></div>
  <div class="faq-item" style="top:625px">Why IP Matters to Your StartUp<span class="toggle"><svg width="14" height="14" viewBox="0 0 14 14"><path d="M5 2l5 5-5 5" stroke="#fff" stroke-width="2" fill="none"/></svg></span></div>
</section>

<section class="testimonials">
  <h2 class="section-title" style="top:100px"><b>Client</b> Testimonials</h2>
  <article class="testimonial faded" style="left:-60px">
    <div class="avatar"></div><div class="t-name">Arjun Mehta,</div><div class="t-role">Creative Manager</div>
    <p class="t-quote">Lorem ipsum dolor sit amet, consectetur adipiscing elit, sed do eiusmod tempor incididunt ut labore et dolore magna aliqua. Ut enim ad minim veniam...</p>
  </article>
  <article class="testimonial" style="left:395px">
    <div class="avatar"></div><div class="t-name">Arjun Mehta,</div><div class="t-role">Creative Manager</div>
    <p class="t-quote">Lorem ipsum dolor sit amet, consectetur adipiscing elit, sed do eiusmod tempor incididunt ut labore et dolore magna aliqua. Ut enim ad minim veniam...</p>
  </article>
  <article class="testimonial faded" style="left:838px">
    <div class="avatar"></div><div class="t-name">Arjun Mehta,</div><div class="t-role">Creative Manager</div>
    <p class="t-quote">Lorem ipsum dolor sit amet, consectetur adipiscing elit, sed do eiusmod tempor incididunt ut labore et dolore magna aliqua. Ut enim ad minim veniam...</p>
  </article>
  <span class="slider-arrow prev"><svg width="16" height="16" viewBox="0 0 16 16"><path d="M10 3L5 8l5 5" stroke="#ec1f27" stroke-width="2.4" fill="none"/></svg></span>
  <span class="slider-arrow next"><svg width="16" height="16" viewBox="0 0 16 16"><path d="M6 3l5 5-5 5" stroke="#fff" stroke-width="2.4" fill="none"/></svg></span>
</section>

<div class="lawyer-photo" role="img" aria-label="Portrait of Daniel R. Hartley in a suit"></div>
<section class="lawyer-band">
  <div class="abs lawyer-name">Daniel R. Hartley,<em>Canadian Patent Lawyer</em></div>
  <p class="abs lawyer-desc">Daniel is an intellectual property lawyer with the firm's Technology and Intellectual Property practice groups.</p>
  <span class="btn">Contact us
    <svg width="14" height="14" viewBox="0 0 16 16"><circle cx="8" cy="8" r="7" fill="#ec1f27"/><path d="M6.5 4.5l3.5 3.5-3.5 3.5" stroke="#fff" stroke-width="2" fill="none"/></svg></span>
</section>

<section class="partners">
  <h2 class="section-title" style="top:92px"><b>Our</b> Partners</h2>
  <svg class="partner-arrow" style="left:78px" width="16" height="22" viewBox="0 0 16 22"><path d="M12 3L4 11l8 8" stroke="#666" stroke-width="2" fill="none"/></svg>
  <div class="partner" style="left:115px"><span></span></div>
  <div class="partner" style="left:315px"><span></span></div>
  <div class="partner" style="left:515px"><span></span></div>
  <div class="partner" style="left:715px"><span></span></div>
  <div class="partner" style="left:915px"><span></span></div>
  <svg class="partner-arrow" style="left:1105px" width="16" height="22" viewBox="0 0 16 22"><path d="M4 3l8 8-8 8" stroke="#666" stroke-width="2" fill="none"/></svg>
</section>

<section class="consult">
  <h2 class="section-title" style="top:95px"><b>Free</b> Consultation</h2>
  <p class="section-sub" style="top:150px">Don't hesitate to reach out if you have any questions.</p>
  <div class="call-btn">Call (416) 555-0142</div>
  <div class="field" style="left:200px;top:250px;width:258px">Enter Name</div>
  <div class="field" style="left:471px;top:250px;width:258px">Email Address</div>
  <div class="field" style="left:742px;top:250px;width:258px">Phone</div>
  <div class="field" style="left:200px;top:308px;width:800px;height:72px">Message</div>
  <span class="btn btn-red">Submit now</span>
</section>

<footer class="site-footer">
  <div class="abs footer-brand"><div class="brand-mark"></div><div class="brand-name">ipnorthlegal</div></div>
  <div class="footer-col" style="left:440px">
    <h5>Contact Us</h5>
    <ul class="contact-list">
      <li><svg width="16" height="16" viewBox="0 0 24 24"><path fill="#fff" d="M12 2a7 7 0 00-7 7c0 5 7 13 7 13s7-8 7-13a7 7 0 00-7-7zm0 9.5A2.5 2.5 0 1112 6.5a2.5 2.5 0 010 5z"/></svg><span>120 Harbour Lane, M5J 1A7<br>Toronto, Ontario.</span></li>
      <li><svg width="16" height="16" viewBox="0 0 24 24"><path fill="#fff" d="M6.6 10.8a15.1 15.1 0 006.6 6.6l2.2-2.2a1 1 0 011-.25 11.4 11.4 0 003.6.57 1 1 0 011 1V20a1 1 0 01-1 1A17 17 0 013 4a1 1 0 011-1h3.5a1 1 0 011 1 11.4 11.4 0 00.57 3.6 1 1 0 01-.25 1z"/></svg><span>(416) 555-0142</span></li>
      <li><svg width="16" height="16" viewBox="0 0 24 24"><path fill="#fff" d="M3 5h18v14H3zm2 2v.5l7 4.5 7-4.5V7l-7 4.5z"/></svg><span>info@ipnorthlegal.com</span></li>
    </ul>
  </div>
  <div class="footer-col" style="left:738px">
    <h5>Quick Links</h5>
    <ul><li>» Home</li><li>» About Us</li><li>» Services</li><li>» Our Team</li></ul>
  </div>
  <div class="footer-col" style="left:935px">
    <h5>Resources</h5>
    <ul><li>» Latest News</li><li>» Clients</li><li>» FAQs</li><li>» Contact Us</li></ul>
  </div>
  <div class="abs footer-rule"></div>
  <div class="abs socials"><span></span><span></span><span></span><span></span></div>
  <p class="abs copyright">Copyright © 2019 ipnorthlegal. All Rights Reserved.</p>
</footer>

</body>
</html>
```